Unique Business Card Design

Unique Business Card design for our orthotic and prosthetic company. Our logo is on our website, color is light blue. Unique shape (artificial leg shaped, vertical, etc..) preferred. Logo, business name, individual name and basic demographics needed.

Industry/Entity Type

Business

Contact Information for Business Card

Logo, Industry, Phone # Logo, "Prosthetic & Orthotic Services" Place to add individual name and contact info

Colors
cee9f5

Requirements
Must have
• The icon must be there, placement of "Prosthetic & Orthotic Services" can be moved
Nice to have
• Like the mix of light blue, and a little darker blue. One design included the icons from my website which was a nice touch

```html
<!DOCTYPE html>
<html lang="en">
<head>
<meta charset="utf-8">
<title>Limbwise Inc — Business Card</title>
<link href="https://fonts.googleapis.com/css2?family=Open+Sans:wght@400;600;700&family=Lora:ital@1&display=swap" rel="stylesheet">
<style>
  :root {
    --page-bg: #e9e6e1;
    --brand-blue: #0f5db3;
    --brand-blue-soft: #1f6cc0;
    --mid-blue: #1a72c9;
    --pale-blue: #d3eaf6;
    --text-dark: #3a3a3a;
    --white: #ffffff;
  }
  * { box-sizing: border-box; margin: 0; padding: 0; }
  html, body { width: 1200px; height: 900px; overflow: hidden; }
  body {
    background: var(--page-bg);
    font-family: "Open Sans", Arial, sans-serif;
    position: relative;
  }
  .card {
    position: absolute;
    width: 560px;
    height: 320px;
    border-radius: 2px;
    box-shadow: 0 6px 18px rgba(0,0,0,0.18);
    overflow: hidden;
  }
  /* Front card */
  .card--front {
    left: 50px; top: 120px;
    background: var(--brand-blue);
  }
  .card--front .pattern-area {
    position: absolute; inset: 0;
    background: linear-gradient(135deg, var(--brand-blue) 0%, var(--brand-blue-soft) 100%);
  }
  .card--front .brand {
    position: absolute; left: 60px; top: 88px;
    display: flex; align-items: center; gap: 26px;
  }
  .brand-dot {
    flex: none;
    border-radius: 50%;
  }
  .card--front .brand-dot {
    width: 120px; height: 120px; background: var(--white);
  }
  .brand-name {
    font-weight: 600;
    letter-spacing: 0.5px;
    line-height: 1;
    padding-bottom: 6px;
  }
  .card--front .brand-name {
    color: var(--white); font-size: 30px;
    border-bottom: 2px solid var(--white);
  }
  .tagline {
    font-family: "Lora", Georgia, serif;
    font-style: italic;
    margin-top: 6px;
    padding-left: 20px;
  }
  .card--front .tagline { color: var(--white); font-size: 15px; }
  .card--front .website {
    position: absolute; left: 0; right: 0; bottom: 40px;
    text-align: center; color: var(--white);
    font-size: 15px; font-weight: 600;
  }
  /* Back card */
  .card--back {
    left: 590px; top: 450px;
    background: var(--pale-blue);
  }
  .contact {
    position: absolute; left: 260px; top: 28px;
    color: var(--text-dark); font-size: 14px; line-height: 1.4;
  }
  .contact .person-name {
    color: var(--mid-blue); font-weight: 700; font-size: 17px;
  }
  .contact .role { margin-left: 6px; }
  .contact .address { margin-left: 14px; }
  .contact-list { list-style: none; margin-left: 36px; margin-top: 2px; }
  .contact-list li { display: flex; align-items: center; gap: 8px; }
  .contact-list .phone { font-weight: 700; }
  .contact-list svg { width: 12px; height: 12px; fill: var(--mid-blue); flex: none; }
  .card--back .brand {
    position: absolute; left: 34px; top: 170px;
    display: flex; align-items: center; gap: 22px;
  }
  .card--back .brand-dot {
    width: 140px; height: 140px; background: var(--mid-blue);
  }
  .card--back .brand-name {
    color: var(--mid-blue); font-size: 32px;
    border-bottom: 2px solid var(--mid-blue);
  }
  .card--back .tagline { color: var(--mid-blue); font-size: 15px; }
</style>
</head>
<body>

  <section class="card card--front">
    <div class="pattern-area" role="img" aria-label="Repeating pattern of faint brand marks across the blue background"></div>
    <div class="brand">
      <span class="brand-dot"></span>
      <div>
        <div class="brand-name">LIMBWISE INC</div>
        <div class="tagline">Prosthetic &amp; Orthotic Services</div>
      </div>
    </div>
    <div class="website">www.limbwiseinc.com</div>
  </section>

  <section class="card card--back">
    <div class="contact">
      <div class="person-name">DANIEL REYES</div>
      <div class="role">Managing Director</div>
      <div class="address">12345, Address Goes Here<br>Country Name, 123456.</div>
      <ul class="contact-list">
        <li class="phone">
          <svg viewBox="0 0 12 12" aria-hidden="true"><path d="M1 3c0-1 1-2 5-2s5 1 5 2v1H8V3H4v1H1zM3 5h6l2 5H1z"/></svg>
          (555) 014-2290
        </li>
        <li>
          <svg viewBox="0 0 12 12" aria-hidden="true"><path d="M0 2h12v8H0zM1 3l5 4 5-4z" fill-rule="evenodd"/></svg>
          info@limbwiseinc.com
        </li>
        <li>
          <svg viewBox="0 0 12 12" aria-hidden="true"><path d="M3 9l6-6M2 7l-1 1a2 2 0 0 0 3 3l1-1M10 5l1-1a2 2 0 0 0-3-3L7 2" stroke="#1a72c9" stroke-width="1.4" fill="none"/></svg>
          www.limbwiseinc.com
        </li>
      </ul>
    </div>
    <div class="brand">
      <span class="brand-dot"></span>
      <div>
        <div class="brand-name">LIMBWISE INC</div>
        <div class="tagline">Prosthetic &amp; Orthotic Services</div>
      </div>
    </div>
  </section>

</body>
</html>
```